VoIP Unified Communications Service Flyer

I need a trifold brochure made for my VoIP services describing the advantages of switching over to VoIP Unified Communications, I want our current logo, and contact info, as well as the color scheme that we use with the logo, which is gray, and orange, also a picture of the Korvane DXP M41H phone should be used as an example of the phones we provide. The trifold brochure should be printable on 8.5 by 11inch paper, I uploaded some of the images that if modified so I am not plagiarizing, could help for the 3 inner folds.

Target Market(s)

Businesses

Industry/Entity Type

Telecommunications

Font styles to use
Serif
Sans Serif

Requirements
Must have
• Top Reasons to move to VoIP Unified Communications Service, a picture of a Korvane DXP M41H Phone, contact info on the back, company name and logo in the top, one of the reasons should be, we are a local company, and we offer immediate US based support.
Nice to have
• Contact info:

O: (575) 804-3162
C: (575) 462-0571
E: info@pelmorasystems.com
W: https://pelmorasystems.com
FB: https://facebook.com/pelmorasystems

```html
<!DOCTYPE html>
<html lang="en">
<head>
<meta charset="utf-8">
<title>Pelmora Systems – Trifold Brochure</title>
<link href="https://fonts.googleapis.com/css2?family=Montserrat:wght@400;500;700;800&display=swap" rel="stylesheet">
<style>
:root{
  --orange:#ee5a24;
  --orange-soft:#f58a3c;
  --charcoal:#3a3a3a;
  --ink:#2b2b2b;
  --paper:#ffffff;
  --backdrop:#2f3033;
  --muted-on-dark:#e4e4e4;
}
*{box-sizing:border-box;margin:0;padding:0}
html,body{width:1069px;height:1200px;overflow:hidden;background:var(--backdrop)}
body{font-family:"Montserrat",sans-serif;color:var(--ink);position:relative}
.spread{position:absolute;left:132px;width:805px;height:570px;background:var(--paper);overflow:hidden}
.spread--outer{top:20px}
.spread--inner{top:610px}
.art{position:absolute;inset:0}
.abs{position:absolute}
h3{font-weight:800;color:var(--orange);text-transform:uppercase;line-height:1.05}
p{font-size:8.2px;line-height:1.36;text-align:justify}

/* outer */
.vision{left:23px;top:428px;width:225px}
.vision h3{font-size:14px;margin-bottom:6px}
.contact{left:292px;top:452px;width:250px}
.contact h3{font-size:14px;margin-bottom:7px}
.contact li{list-style:none;font-size:12px;line-height:17px;display:flex;align-items:center;gap:8px}
.contact svg{flex:none}
.brand{left:563px;top:440px;width:235px}
.brand-name{display:flex;align-items:center;gap:7px;font-size:15px;font-weight:500;color:var(--orange);letter-spacing:2px;margin-bottom:12px}
.brand-mark{width:16px;height:16px;border-radius:50%;background:var(--charcoal)}
.brand h3{font-size:14.5px;border-bottom:1.5px solid var(--orange);display:inline-block;padding-bottom:2px;margin-bottom:5px}
.brand .tagline{font-size:10px;font-weight:700;text-transform:uppercase;line-height:1.3;text-align:left}

/* inner */
.features{left:23px;top:172px;width:222px}
.feature{margin-bottom:12px}
.feature-head{display:flex;align-items:center;gap:9px;margin-bottom:6px}
.feature-head h3{font-size:11.5px}
.reasons{left:290px;top:18px;width:224px}
.reasons h3,.extras h3{font-size:13.5px;margin-bottom:3px;white-space:nowrap}
.reasons p,.extras p{font-size:7.8px}
.reasons .item{margin-bottom:6px}
.extras{left:560px;top:18px;width:224px}
.extras .item{margin-bottom:7px}
.dark-list{left:568px;top:196px;width:216px}
.dark-list h3{font-size:12.5px;margin-bottom:3px}
.dark-list p{color:var(--muted-on-dark);font-size:7.2px;line-height:1.35;margin-bottom:8px}
</style>
</head>
<body>

<!-- OUTER SPREAD -->
<section class="spread spread--outer">
  <svg class="art" width="805" height="570" viewBox="0 0 805 570">
    <defs>
      <linearGradient id="gTeal" x1="0" y1="0" x2="1" y2="1"><stop offset="0" stop-color="#7fd3d6"/><stop offset=".6" stop-color="#3a7f8c"/><stop offset="1" stop-color="#1c2f3a"/></linearGradient>
      <linearGradient id="gCity" x1="0" y1="0" x2="0" y2="1"><stop offset="0" stop-color="#c9d6e4"/><stop offset=".5" stop-color="#6d7683"/><stop offset="1" stop-color="#2d3036"/></linearGradient>
      <linearGradient id="gHand" x1="0" y1="0" x2="1" y2="1"><stop offset="0" stop-color="#3b3f8f"/><stop offset="1" stop-color="#62c2d8"/></linearGradient>
      <linearGradient id="gPhone" x1="0" y1="0" x2="1" y2="1"><stop offset="0" stop-color="#e7c0a0"/><stop offset=".5" stop-color="#d9d9d9"/><stop offset="1" stop-color="#5a5a5a"/></linearGradient>
    </defs>
    <circle cx="594" cy="165" r="248" fill="none" stroke="var(--orange)" stroke-width="4" stroke-dasharray="900 1000" transform="rotate(60 594 165)"/>
    <circle cx="594" cy="165" r="240" fill="url(#gCity)" stroke="#fff" stroke-width="4" role="img" aria-label="Photo: city skyline at night overlaid with glowing circuit lines and technology icons"/>
    <circle cx="230" cy="212" r="195" fill="none" stroke="var(--orange)" stroke-width="4" stroke-dasharray="500 1000" transform="rotate(-100 230 212)"/>
    <circle cx="230" cy="208" r="187" fill="url(#gTeal)" stroke="#fff" stroke-width="5" role="img" aria-label="Photo: business people and a robot in front of a large data display wall"/>
    <circle cx="91" cy="88" r="84" fill="url(#gHand)" stroke="#fff" stroke-width="5" role="img" aria-label="Photo: hand touching a digital interface"/>
    <circle cx="402" cy="366" r="81" fill="url(#gPhone)" stroke="#fff" stroke-width="5" role="img" aria-label="Photo: hand holding a smartphone beside a bowl of fruit"/>
    <path d="M0 555 C200 545 500 552 805 540 L805 570 L0 570 Z" fill="var(--orange)"/>
    <path d="M0 555 C200 545 500 552 805 540" fill="none" stroke="var(--orange-soft)" stroke-width="2"/>
  </svg>

  <div class="abs vision">
    <h3>Our Vision &amp;<br>Values</h3>
    <p>Customer satisfaction, openness, innovation, teamwork and growth are the core values behind our company. We continue to reflect who we are, how we work, and what we strive for.</p>
  </div>

  <div class="abs contact">
    <h3>Contact Us</h3>
    <ul>
      <li><svg width="10" height="10" viewBox="0 0 24 24"><path d="M6 2l4 5-2 3c1 3 3 5 6 6l3-2 5 4-3 4C10 22 2 14 2 5z" fill="none" stroke="var(--orange)" stroke-width="2.4"/></svg>(575) 804-3162</li>
      <li><svg width="10" height="10" viewBox="0 0 24 24"><circle cx="12" cy="12" r="10" fill="none" stroke="var(--orange)" stroke-width="2.4"/><rect x="7" y="8" width="10" height="8" fill="none" stroke="var(--orange)" stroke-width="2"/></svg>support@pelmorasystems.com</li>
      <li><svg width="10" height="10" viewBox="0 0 24 24"><circle cx="12" cy="12" r="10" fill="none" stroke="var(--orange)" stroke-width="2.4"/><path d="M2 12h20M12 2c4 4 4 16 0 20M12 2c-4 4-4 16 0 20" fill="none" stroke="var(--orange)" stroke-width="1.6"/></svg>www.pelmorasystems.com</li>
    </ul>
  </div>

  <div class="abs brand">
    <div class="brand-name"><span class="brand-mark"></span>PELMORA SYSTEMS</div>
    <h3>Professional<br>Computer Services</h3>
    <p class="tagline">We make computer and technology<br>services accessible!</p>
  </div>
</section>

<!-- INNER SPREAD -->
<section class="spread spread--inner">
  <svg class="art" width="805" height="570" viewBox="0 0 805 570">
    <defs>
      <linearGradient id="gDesk" x1="0" y1="0" x2="1" y2="1"><stop offset="0" stop-color="#f2f2f2"/><stop offset=".6" stop-color="#b8bcc2"/><stop offset="1" stop-color="#5c5f66"/></linearGradient>
    </defs>
    <path d="M0 0 H268 V170 C200 150 120 140 0 155 Z" fill="url(#gDesk)" role="img" aria-label="Photo: person using a tablet at a desk with a cup of coffee"/>
    <path d="M0 155 C120 140 200 150 268 170 L268 180 C200 158 120 150 0 165 Z" fill="var(--orange)"/>
    <path d="M538 182 C620 180 700 182 755 170 C780 165 795 160 805 150 L805 570 L538 570 Z" fill="var(--charcoal)"/>
    <path d="M755 170 C780 165 795 160 805 150 L805 160 C795 170 780 175 760 178 Z" fill="var(--orange)"/>
    <path d="M0 556 C250 554 550 552 805 540 L805 570 L0 570 Z" fill="var(--orange)"/>
  </svg>

  <div class="abs features">
    <div class="feature"><div class="feature-head"><svg width="22" height="22" viewBox="0 0 24 24"><circle cx="12" cy="12" r="10" fill="none" stroke="var(--orange)" stroke-width="1.6"/><path d="M8 16l8-8M11 8h5v5" fill="none" stroke="var(--orange)" stroke-width="1.6"/></svg><h3>Scalable</h3></div><p>Customer satisfaction, openness, innovation, teamwork and growth are the core values behind our company. We continue to reflect who we are, how we work, and what we strive for.</p></div>
    <div class="feature"><div class="feature-head"><svg width="22" height="22" viewBox="0 0 24 24"><circle cx="12" cy="12" r="10" fill="none" stroke="var(--orange)" stroke-width="1.6"/><path d="M12 6v12M15 9h-4a2 2 0 000 4h2a2 2 0 010 4H9" fill="none" stroke="var(--orange)" stroke-width="1.6"/></svg><h3>Surprisingly Affordable</h3></div><p>Slash your current business phone bill by -60%. The best virtual phone features can now be yours</p></div>
    <div class="feature"><div class="feature-head"><svg width="22" height="22" viewBox="0 0 24 24"><circle cx="12" cy="12" r="10" fill="none" stroke="var(--orange)" stroke-width="1.6"/><path d="M7 12l3 3 7-7" fill="none" stroke="var(--orange)" stroke-width="1.8"/></svg><h3>Amazing Service</h3></div><p>Receive the best support from our 100% in- house team. Your business needs are our top priority. Learn more about Amazing Service</p></div>
    <div class="feature"><div class="feature-head"><svg width="22" height="22" viewBox="0 0 24 24"><circle cx="12" cy="12" r="10" fill="none" stroke="var(--orange)" stroke-width="1.6"/><path d="M12 6l5 2v4c0 3-2 5-5 6-3-1-5-3-5-6V8z" fill="none" stroke="var(--orange)" stroke-width="1.6"/></svg><h3>Reliable</h3></div><p>Always stay connected with our highly redundant network. We're proud to be a service provider with 99.999% uptime, 24/7.</p></div>
    <div class="feature"><div class="feature-head"><svg width="22" height="22" viewBox="0 0 24 24"><circle cx="12" cy="12" r="10" fill="none" stroke="var(--orange)" stroke-width="1.6"/><path d="M7 15a3 3 0 010-6 4 4 0 018-1 3 3 0 012 7z" fill="none" stroke="var(--orange)" stroke-width="1.6"/></svg><h3>Hosted PBX</h3></div><p>Make calls and manage your phone system from anywhere. Goodbye, landlines. Hello, productivity!</p></div>
  </div>

  <div class="abs reasons">
    <div class="item"><h3>Saves You Money</h3><p>Customers of Corliant's small business VoIP phone service typically experience savings of up to 60% on their monthly phone bill</p></div>
    <div class="item"><h3>Secure Network</h3><p>A scalable network developed by over 1,500 engineers powers Corliant business VoIP phone service. We promise top quality, security, and reliability</p></div>
    <div class="item"><h3>Designed for All Industries</h3><p>There's something for everyone. Our small business VoIP features benefit all industries, including insurance, hospitality, consulting firms, real estate, education, health care, and more!</p></div>
    <div class="item"><h3>Innovation</h3><p>We are always innovating and improving our VoIP phone service. Your small business will always have the latest and greatest in business VoIP technology and phone systems.</p></div>
    <div class="item"><h3>Amazing Service</h3><p>We are committed to delivering Amazing Service to your small business, at every point of contact you make with Corliant. This is our brand promise.</p></div>
    <div class="item"><h3>Mobile Friendly</h3><p>Run your small business anywhere with the Corliant app. Seamlessly text message your customers and team members right from your smartphone. Feel the power of business VoIP right at your fingertips.</p></div>
    <div class="item"><h3>HD Quality VoIP</h3><p>Experience crystal-clear HD voice quality with Corliant's small business VoIP phone service. You'll never have to worry about poor call quality ever again.</p></div>
    <div class="item"><h3>Powerful Features</h3><p>Get enterprise-grade business VoIP features without the hefty price tag. Auto-attendant, business text messaging, caller ID, voicemail to text, CRM integration, and much more</p></div>
  </div>

  <div class="abs extras">
    <div class="item"><h3>Easy to Use</h3><p>Our business VoIP phones are so easy to use, you'll be up and running within minutes. You don't need to be a tech wizard or have an IT department to get the most out of your phone system. Corliant was designed for non-technical small business owners</p></div>
    <div class="item"><h3>Honest Pricing</h3><p>Our customers know what they're paying for. No contracts required, no hidden fees. You can cancel your service at any time, hassle-free.</p></div>
  </div>

  <div class="abs dark-list">
    <h3>Corliant App</h3><p>Get the Corliant desktop app or Android / iOS app on your mobile device. Start chatting with your teams and customers with a fast internet connection!</p>
    <h3>Auto Attendant</h3><p>Let Corliant's auto attendant feature streamline your call routing. You can also apply call forwarding to your auto attendant</p>
    <h3>Call Queuing</h3><p>Route phone calls to the right department with Corliant's phone solution. Instantly turn on call waiting, voicemail, and call forwarding for incoming calls</p>
    <h3>Text Messaging</h3><p>Send texts from your WiFi-enabled mobile phone or desktop. Get unlimited texting to and from your business phone number.</p>
    <h3>Voicemail to Email</h3><p>Now it's easy to listen to voicemail messages on the go from your email account. Listen to call recordings on your mobile app, laptop, or desktop</p>
    <h3>Unlimited Calling</h3><p>No per-minute charges when you place calls to the United States and Canada. Get advanced features like unlimited conference calling, faxing, and SMS messages</p>
  </div>
</section>

</body>
</html>
```